BRAVLO PRESSURE WASHING LLC

am starting a small pressure washing business in myrtle beach. I need a weebsite that will get people attention. I wanrto advertise our services . Main two : We specialize in roof cleaning , window cleaning . Other services are : residential and commercial, driveways & sidewalks, gutter cleaning, patio & deck cleaning, curb appeal, heavy equipment, mobile homes, car lots, fleets, store fronts, commercial buildings, grocery kart sanitizing, have a couple phrases saying. " Make your home shine" " Make your home look new again" I need a section showing our work in the past. Im going to send you some ,before and after pictures of our work. Also put the 100% satisfaction guaranteed ribbon somewhere on the website and give us a call for your free estiment 555 214 6379. Licensed and insured. Also need a page listing our services and a paragraph or two of the importance of that service. Maybe a section where customers can comment and give good reviews. I need it to have my logo and make it look modern and catch the eye . We founded in 2019 and use environmental amd pet friendly chemicals and top of the line pressure washing equipment. Thank you.l

```html
<!DOCTYPE html>
<html lang="en">
<head>
<meta charset="utf-8">
<title>Bravlo Pressure Washing LLC</title>
<link rel="stylesheet" href="https://fonts.googleapis.com/css2?family=Oswald:wght@600;700&family=Poppins:ital,wght@0,300;0,400;0,500;0,600;1,400&family=Roboto:wght@400;500;700&display=swap">
<style>
:root{
  --blue:#1a8bd6;
  --blue-dark:#1273b6;
  --navy:#0b3566;
  --ink:#141414;
  --text:#4a4a4a;
  --muted:#7a7a7a;
  --light:#f3f3f3;
  --footer:#121212;
  --gold:#f3b51b;
  --badge:#c99a2e;
  --white:#ffffff;
}
*{box-sizing:border-box;margin:0;padding:0}
html,body{width:1200px;height:5068px;overflow:hidden}
body{font-family:"Poppins",sans-serif;color:var(--text);background:var(--white);position:relative}
.section{position:relative;width:1200px;overflow:hidden}
.abs{position:absolute}
.btn{position:absolute;display:flex;align-items:center;justify-content:center;background:var(--blue);color:var(--white);font-family:"Roboto",sans-serif;font-weight:700;font-size:16px;border-radius:3px;letter-spacing:.2px}
.heading{font-family:"Oswald",sans-serif;font-weight:700;color:var(--ink);text-align:center;font-size:42px;letter-spacing:.3px;line-height:1}
.rule{width:60px;height:3px;background:var(--blue);margin:0 auto}
.lead{text-align:center;font-size:14px;line-height:26px;color:var(--text)}

/* header */
.site-header{height:94px;background:var(--white);position:relative;z-index:2}
.brand{position:absolute;left:70px;top:0;width:200px;height:118px;background:var(--white);border-radius:0 0 100px 100px;display:flex;align-items:center;justify-content:center;gap:8px}
.brand-dot{width:18px;height:18px;border-radius:50%;background:var(--blue)}
.brand-name{font-family:"Roboto",sans-serif;font-weight:700;color:var(--navy);font-size:30px;line-height:1}
.brand-name small{display:block;font-size:10.5px;letter-spacing:.4px;margin-top:4px}
.main-nav{position:absolute;top:62px;left:408px;display:flex;font-family:"Roboto",sans-serif;font-weight:700;font-size:14px;color:var(--ink)}
.main-nav span{display:block}
.main-nav .n1{color:var(--blue);width:101px}
.main-nav .n2{width:108px}.main-nav .n3{width:129px}.main-nav .n4{width:133px}.main-nav .n5{width:127px}
.follow{position:absolute;top:20px;left:749px;display:flex;align-items:center;gap:7px;font-family:"Roboto",sans-serif;font-weight:700;font-size:9.5px;color:var(--ink)}
.follow .dot{width:28px;height:28px;border-radius:50%;background:var(--blue)}
.follow .dot.navy{background:var(--navy)}
.follow .label{margin-right:6px}
.callbox{position:absolute;left:951px;top:10px;display:flex;gap:8px;align-items:center}
.callbox .small{font-family:"Roboto",sans-serif;font-size:10px;color:var(--ink);font-weight:500}
.callbox .num{font-family:"Roboto",sans-serif;font-size:17px;color:var(--blue);font-weight:500}

/* hero */
.hero{height:566px;background:linear-gradient(100deg,#3c6f8e 0%,#c48a6a 22%,#e2b79a 40%,#b98c74 58%,#6a5a52 80%,#3d3430 100%)}
.hero-photo{position:absolute;inset:0;background:linear-gradient(180deg,rgba(120,150,180,.35) 0%,rgba(0,0,0,0) 40%,rgba(40,25,15,.45) 100%)}
.hero h1{position:absolute;left:508px;top:206px;font-family:"Oswald",sans-serif;font-weight:700;font-size:46px;color:var(--white);letter-spacing:.5px;line-height:1}
.hero p{position:absolute;left:510px;top:272px;font-size:20px;color:var(--white)}
.hero .arrow{position:absolute;top:265px;width:34px;height:34px;border:2px solid rgba(255,255,255,.8);border-radius:50%}
.dots{position:absolute;top:519px;left:560px;display:flex;gap:8px}
.dots i{display:block;width:12px;height:12px;border-radius:50%;background:var(--white)}
.dots i.off{background:transparent;border:2px solid var(--white)}

/* services */
.services{height:735px}
.services .heading{padding-top:124px}
.services .rule{margin-top:18px}
.services .lead{margin-top:18px}
.cards{position:absolute;top:275px;left:100px;display:flex;gap:14px}
.svc{width:239px;height:330px;background:var(--white);box-shadow:0 2px 10px rgba(0,0,0,.13);text-align:center;position:relative}
.svc svg{margin-top:26px}
.svc h3{font-family:"Roboto",sans-serif;font-weight:500;font-size:18px;color:var(--ink);margin-top:18px}
.svc p{font-size:13px;line-height:26px;color:var(--muted);margin:10px 22px 0}
.svc .btn{left:40px;bottom:21px;width:160px;height:46px;font-size:15px}

/* quote band */
.quote{height:320px;background:var(--navy)}
.badge-slot{position:absolute;left:132px;top:92px;width:138px;height:138px;border-radius:50%;background:var(--badge)}
.quote h2{position:absolute;left:312px;top:90px;font-family:"Oswald",sans-serif;font-weight:700;font-size:40px;color:var(--white);line-height:1}
.quote p{position:absolute;left:312px;top:145px;width:510px;font-size:21px;line-height:33px;color:var(--white)}
.quote .btn{left:840px;top:138px;width:232px;height:47px}

/* welcome */
.welcome{height:621px;background:var(--light)}
.welcome-photo{position:absolute;left:0;top:0;width:700px;height:621px;background:linear-gradient(90deg,#8b3a22 0%,#b5502c 35%,#d79a80 62%,rgba(243,243,243,0) 100%)}
.welcome .kicker{position:absolute;left:635px;top:120px;font-family:"Oswald",sans-serif;font-weight:600;font-size:25px;color:var(--ink)}
.welcome h2{position:absolute;left:635px;top:158px;font-family:"Oswald",sans-serif;font-weight:700;font-size:36px;color:var(--ink);line-height:1}
.welcome .rule{position:absolute;left:635px;top:217px;margin:0}
.welcome p{position:absolute;left:635px;top:240px;width:470px;font-size:14px;line-height:27px;color:var(--text)}
.welcome .btn{left:635px;top:450px;width:160px;height:48px}

/* projects */
.projects{height:827px}
.projects .heading{padding-top:141px}
.projects .rule{margin-top:18px}
.projects .lead{margin-top:18px}
.proj-row{position:absolute;top:269px;left:100px;display:flex;gap:17px}
.proj{width:322px;text-align:center}
.proj .img{height:266px;display:flex}
.proj .img div{flex:1}
.proj .img .split{flex:0 0 3px;background:var(--gold)}
.proj h3{font-family:"Roboto",sans-serif;font-weight:500;font-size:21px;color:var(--ink);margin-top:24px;letter-spacing:.3px}
.proj p{font-size:14px;color:var(--muted);margin-top:6px}
.projects .btn{left:464px;top:654px;width:272px;height:50px}

/* reviews */
.reviews{height:687px;background:linear-gradient(180deg,#1d4b80 0%,#163f6f 55%,#10335d 100%)}
.reviews .heading{color:var(--white);padding-top:115px}
.reviews .rule{margin-top:18px}
.reviews .lead{color:var(--white);margin-top:16px;padding:0 270px}
.rev-row{position:absolute;top:272px;left:88px;display:flex;gap:34px}
.rev{width:316px;height:296px;background:var(--white);border-bottom:8px solid var(--blue);position:relative;padding:28px 24px 0}
.stars{display:flex;gap:2px}
.g-dot{position:absolute;right:24px;top:26px;width:28px;height:28px;border-radius:50%;border:4px solid var(--blue)}
.rev p{font-style:italic;font-size:16px;line-height:30px;color:var(--ink);margin-top:26px;text-align:justify}
.rev .who{font-family:"Roboto",sans-serif;font-weight:500;font-size:19px;color:var(--ink);margin-top:16px}

/* blogs */
.blogs{height:770px}
.blogs .heading{padding-top:125px}
.blogs .rule{margin-top:18px}
.blogs .lead{margin-top:18px}
.blog-row{position:absolute;top:272px;left:108px;display:flex;gap:19px}
.blog{width:317px;height:376px;border-bottom:6px solid var(--navy);box-shadow:0 1px 6px rgba(0,0,0,.06)}
.blog.active{border-bottom-color:var(--blue)}
.blog .img{height:223px}
.blog .date{font-size:12px;line-height:18px;color:var(--blue);margin:12px 0 0 16px}
.blog h4{font-family:"Roboto",sans-serif;font-weight:500;font-size:15px;line-height:26px;color:var(--ink);margin:6px 16px 0}
.blog p{font-size:12px;line-height:24px;color:var(--muted);margin:8px 16px 0}

/* footer */
.site-footer{height:468px;background:var(--footer);color:var(--white)}
.foot-brand{position:absolute;left:98px;top:78px;display:flex;align-items:center;gap:10px}
.foot-brand .brand-name{color:var(--white);font-size:34px}
.foot-brand .brand-name small{font-size:12px}
.license{position:absolute;left:110px;top:220px;font-size:13px}
.socials{position:absolute;left:110px;top:254px;display:flex;gap:6px}
.socials i{display:block;width:32px;height:32px;border-radius:50%;background:var(--white)}
.foot-col h5{font-family:"Roboto",sans-serif;font-weight:700;font-size:14.5px;letter-spacing:.3px;margin-bottom:28px}
.foot-col{position:absolute;top:90px;font-size:13.5px}
.links li{list-style:none;line-height:28.5px}
.contact-item{display:flex;gap:10px;margin-bottom:15px;line-height:24px}
.contact-item .ic{flex:0 0 22px;height:22px;border-radius:50%;background:#2b2b2b;display:flex;align-items:center;justify-content:center;margin-top:2px}
.sub-text{line-height:27px;width:280px}
.sub-form{display:flex;margin-top:20px;width:267px;height:46px}
.sub-form .input{flex:1;background:var(--white);color:#8a8a8a;font-size:13px;display:flex;align-items:center;padding-left:16px}
.sub-form .send{width:50px;background:var(--blue);display:flex;align-items:center;justify-content:center}
.foot-bottom{position:absolute;left:0;top:390px;width:1200px;border-top:1px solid #2e2e2e}
.foot-bottom .copy{position:absolute;left:110px;top:28px;font-size:13px}
.foot-bottom .legal{position:absolute;right:106px;top:28px;font-size:13px}
</style>
</head>
<body>

<header class="site-header">
  <div class="brand">
    <span class="brand-dot"></span>
    <div class="brand-name">BRAVLO<small>PRESSURE WASHING</small></div>
  </div>
  <div class="follow">
    <span class="label">FOLLOW US</span>
    <span class="dot"></span><span class="dot"></span><span class="dot navy"></span>
  </div>
  <div class="callbox">
    <svg width="26" height="26" viewBox="0 0 24 24" fill="none" stroke="#1a8bd6" stroke-width="1.8"><path d="M5 3h4l2 5-2.5 1.5a11 11 0 0 0 6 6L16 13l5 2v4a2 2 0 0 1-2 2A17 17 0 0 1 3 5a2 2 0 0 1 2-2z"/></svg>
    <div><div class="small">CALL US</div><div class="num">555-214-6379</div></div>
  </div>
  <nav class="main-nav">
    <span class="n1">HOME</span><span class="n2">ABOUT</span><span class="n3">SERVICES</span><span class="n4">PROJECTS</span><span class="n5">REVIEWS</span><span>CONTACT US</span>
  </nav>
</header>

<section class="section hero" role="img" aria-label="Row of colourful beach houses at sunset">
  <div class="hero-photo"></div>
  <span class="arrow" style="left:24px"></span>
  <span class="arrow" style="right:24px"></span>
  <h1>MAKE YOUR HOME SHINE</h1>
  <p>Residential and Commercial Pressure Washing Services</p>
  <div class="btn" style="left:510px;top:326px;width:235px;height:50px;">GET A FREE ESTIMATE</div>
  <div class="dots"><i></i><i></i><i class="off"></i><i></i></div>
</section>

<section class="section services">
  <h2 class="heading">OUR SERVICES</h2>
  <div class="rule"></div>
  <p class="lead">Lorem ipsum dolor sit amet, consectetur adipiscing elit, sed do eiusmod tempor incididunt ut<br>labore et dolore magna aliqua. Quis ipsum suspendisse ultrices gravida.</p>
  <div class="cards">
    <div class="svc">
      <svg width="58" height="52" viewBox="0 0 58 52" fill="none" stroke="#1a8bd6" stroke-width="2"><rect x="3" y="3" width="52" height="46"/><path d="M3 14h52M3 26h52M3 38h52M16 3v46M29 3v46M42 3v46"/></svg>
      <h3>ROOF CLEANING</h3>
      <p>Lorem ips sit ameconsectetur adipiscg elit, sed do eiusmod tempor incididunt ut labore ete magna aliqua.</p>
      <div class="btn">LEARN MORE</div>
    </div>
    <div class="svc">
      <svg width="58" height="52" viewBox="0 0 58 52" fill="none" stroke="#1a8bd6" stroke-width="2"><rect x="10" y="2" width="38" height="48"/><path d="M29 2v48M10 22h38M16 8l6 6M34 28l6 6"/></svg>
      <h3>WINDOW CLEANING</h3>
      <p>Lorem ips sit ameconsectetur adipiscg elit, sed do eiusmod tempor incididunt ut labore ete magna aliqua.</p>
      <div class="btn">LEARN MORE</div>
    </div>
    <div class="svc">
      <svg width="58" height="52" viewBox="0 0 58 52" fill="none" stroke="#1a8bd6" stroke-width="2"><path d="M4 24L29 4l25 20M10 19v29h38V19"/><rect x="24" y="32" width="10" height="16"/><rect x="14" y="26" width="7" height="7"/><rect x="37" y="26" width="7" height="7"/></svg>
      <h3>RESIDENTIAL</h3>
      <p>Lorem ips sit ameconsectetur adipiscg elit, sed do eiusmod tempor incididunt ut labore ete magna aliqua.</p>
      <div class="btn">LEARN MORE</div>
    </div>
    <div class="svc">
      <svg width="70" height="52" viewBox="0 0 70 52" fill="none" stroke="#1a8bd6" stroke-width="2"><rect x="4" y="16" width="16" height="34"/><rect x="22" y="4" width="26" height="46"/><rect x="50" y="16" width="16" height="34"/><path d="M27 11h4M39 11h4M27 20h4M39 20h4M27 29h4M39 29h4M8 24h8M8 32h8M54 24h8M54 32h8M31 50v-10h8v10"/></svg>
      <h3>COMMERCIAL</h3>
      <p>Lorem ips sit ameconsectetur adipiscg elit, sed do eiusmod tempor incididunt ut labore ete magna aliqua.</p>
      <div class="btn">LEARN MORE</div>
    </div>
  </div>
</section>

<section class="section quote">
  <div class="badge-slot" role="img" aria-label="Satisfaction guarantee badge"></div>
  <h2>CALL US FOR FREE QUOTE</h2>
  <p>10% off your next visit with referrals. call now for your free Estimate 555-214-6379Licensed : 2083417 , insured : 376520</p>
  <div class="btn">GET A FREE ESTIMATE</div>
</section>

<section class="section welcome">
  <div class="welcome-photo" role="img" aria-label="Worker pressure washing a red tile roof"></div>
  <div class="kicker">WELCOME TO</div>
  <h2>BRAVLO PRESSURE WASHING LLC</h2>
  <div class="rule"></div>
  <p>Lorem ipsum dolor sit amet, consectetur adipiscing elit, sed do eiusmod tempor incididunt ut labore et dolore ma . Quis ipsum suspendisse ultrices gravida. Risudo viverras accumsan lacus vel facilisis. Lorem ipsum r sit met, consectetur adipisg elit, sed do eiusmod tempor incididunt ut labore et dolore magna aliqua. Quis ipsum suspendisse ultrices gravida. Risusmodo viverra maecenas accumsan lacus vel facilisis.</p>
  <div class="btn">LEARN MORE</div>
</section>

<section class="section projects">
  <h2 class="heading">RECENT PROJECTS</h2>
  <div class="rule"></div>
  <p class="lead">Lorem ipsum dolor sit amet, consectetur adipiscing elit, sed do eiusmod tempor incididunt ut<br>labore et dolore magna aliqua. Quis ipsum suspendisse ultrices gravida.</p>
  <div class="proj-row">
    <div class="proj">
      <div class="img" role="img" aria-label="Driveway before and after washing">
        <div style="background:linear-gradient(180deg,#7a8c6a,#6f6d66)"></div><span class="split"></span><div style="background:linear-gradient(180deg,#8da080,#b8b7b0)"></div>
      </div>
      <h3>DEBRIS REMOVAL</h3><p>Gutter Cleaning in Cheshire,CT</p>
    </div>
    <div class="proj">
      <div class="img" role="img" aria-label="Concrete driveway before and after washing">
        <div style="background:linear-gradient(180deg,#6e8a5e,#5d5a52)"></div><span class="split"></span><div style="background:linear-gradient(180deg,#7d9a6a,#a7a69f)"></div>
      </div>
      <h3>DEBRIS REMOVAL</h3><p>Gutter Cleaning in Cheshire,CT</p>
    </div>
    <div class="proj">
      <div class="img" role="img" aria-label="House roof before and after cleaning">
        <div style="background:linear-gradient(180deg,#9aa6ad,#4c4c4a 45%,#6f7f58)"></div><span class="split"></span><div style="background:linear-gradient(180deg,#a2aeb4,#8a7e70 45%,#7b8c5e)"></div>
      </div>
      <h3>DEBRIS REMOVAL</h3><p>Gutter Cleaning in Cheshire,CT</p>
    </div>
  </div>
  <div class="btn">SEE ALL RECENT PROJECTS</div>
</section>

<section class="section reviews" aria-label="Customer reviews over a house background">
  <h2 class="heading">CUSTOMER REVIEWS</h2>
  <div class="rule"></div>
  <p class="lead">Lorem ipsum dolor sit amet, consectetur adipiscing elit, sed do eiusmod tempor incididunt ut labore et dolore magna aliqua. Quis ipsum suspendisse ultrices gravida.</p>
  <div class="rev-row">
    <div class="rev">
      <div class="stars"><svg width="92" height="16" viewBox="0 0 92 16" fill="#f3b51b"><path id="st" d="M8 0l2.4 5.2 5.6.6-4.2 3.8 1.2 5.6L8 12.4 3 15.2l1.2-5.6L0 5.8l5.6-.6z"/><use href="#st" x="19"/><use href="#st" x="38"/><use href="#st" x="57"/><use href="#st" x="76"/></svg></div>
      <span class="g-dot"></span>
      <p>Lorem ictetur adipiscing elit, sed do eiusmod tempor incididunt ut labore et dolore magna aliqua. Quis ipsum suspendisse ultrices gravida.</p>
      <div class="who">- Sam Rivers</div>
    </div>
    <div class="rev">
      <div class="stars"><svg width="92" height="16" viewBox="0 0 92 16" fill="#f3b51b"><use href="#st"/><use href="#st" x="19"/><use href="#st" x="38"/><use href="#st" x="57"/><use href="#st" x="76"/></svg></div>
      <span class="g-dot"></span>
      <p>Lorem ictetur adipiscing elit, sed do eiusmod tempor incididunt ut labore et dolore magna aliqua. Quis ipsum suspendisse ultrices gravida.</p>
      <div class="who">- Sam Rivers</div>
    </div>
    <div class="rev">
      <div class="stars"><svg width="92" height="16" viewBox="0 0 92 16" fill="#f3b51b"><use href="#st"/><use href="#st" x="19"/><use href="#st" x="38"/><use href="#st" x="57"/><use href="#st" x="76"/></svg></div>
      <span class="g-dot"></span>
      <p>Lorem ictetur adipiscing elit, sed do eiusmod tempor incididunt ut labore et dolore magna aliqua. Quis ipsum suspendisse ultrices gravida.</p>
      <div class="who">- Sam Rivers</div>
    </div>
  </div>
</section>

<section class="section blogs">
  <h2 class="heading">RECENT BLOGS</h2>
  <div class="rule"></div>
  <p class="lead">Lorem ipsum dolor sit amet, consectetur adipiscing elit, sed do eiusmod tempor incididunt ut<br>labore et dolore magna aliqua. Quis ipsum suspendisse ultrices gravida.</p>
  <div class="blog-row">
    <article class="blog">
      <div class="img" role="img" aria-label="Brick storefront with arched windows" style="background:linear-gradient(180deg,#5a2e22,#8c4a34 50%,#c9bfb6)"></div>
      <div class="date">08 OCT 2020</div>
      <h4>Lorem ipsum dolsit amconsectetur adipiscing elit, sed do</h4>
      <p>Lorem ipsum dolor sit amet, consectetur adipiscing elit, sed do eiusmod ....</p>
    </article>
    <article class="blog active">
      <div class="img" role="img" aria-label="Worker cleaning a gutter near a tree" style="background:linear-gradient(180deg,#5f9bd0,#3f6e3a 50%,#7f8c8c)"></div>
      <div class="date">08 AUG 2020</div>
      <h4>Lorem ipsum dolsit amconsectetur adipiscing elit, sed do</h4>
      <p>Lorem ipsum dolor sit amet, consectetur adipiscing elit, sed do eiusmod ....</p>
    </article>
    <article class="blog">
      <div class="img" role="img" aria-label="Cleaner washing a large window" style="background:linear-gradient(90deg,#dfe6ea,#f3f5f6 50%,#7f9ab4)"></div>
      <div class="date">08 AUG 2020</div>
      <h4>Lorem ipsum dolsit amconsectetur adipiscing elit, sed do</h4>
      <p>Lorem ipsum dolor sit amet, consectetur adipiscing elit, sed do eiusmod ....</p>
    </article>
  </div>
</section>

<footer class="section site-footer">
  <div class="foot-brand">
    <span class="brand-dot"></span>
    <div class="brand-name">BRAVLO<small>PRESSURE WASHING</small></div>
  </div>
  <div class="license">CSLB LICENSE # 2083417</div>
  <div class="socials"><i></i><i></i><i></i><i></i></div>

  <div class="foot-col" style="left:340px">
    <h5>QUICK LINKS</h5>
    <ul class="links"><li>Home</li><li>About</li><li>Services</li><li>Projects</li><li>Reviews</li><li>Contact Us</li></ul>
  </div>

  <div class="foot-col" style="left:508px;width:300px">
    <h5>CONTACT US</h5>
    <div class="contact-item"><span class="ic"><svg width="10" height="12" viewBox="0 0 10 12" fill="#fff"><path d="M5 0a4 4 0 0 1 4 4c0 3-4 8-4 8S1 7 1 4a4 4 0 0 1 4-4z"/></svg></span><span>412 Harbor View Lane Myrtle<br>Beach, SC 29577</span></div>
    <div class="contact-item"><span class="ic"><svg width="10" height="10" viewBox="0 0 24 24" fill="#fff"><path d="M5 3h4l2 5-2.5 1.5a11 11 0 0 0 6 6L16 13l5 2v4a2 2 0 0 1-2 2A17 17 0 0 1 3 5a2 2 0 0 1 2-2z"/></svg></span><span>555-214-6379</span></div>
    <div class="contact-item"><span class="ic"><svg width="11" height="8" viewBox="0 0 11 8" fill="none" stroke="#fff"><rect x=".5" y=".5" width="10" height="7"/><path d="M.5.5l5 4 5-4"/></svg></span><span>info@bravlowashpro.com</span></div>
    <div class="contact-item"><span class="ic"><svg width="10" height="10" viewBox="0 0 10 10" fill="none" stroke="#fff"><circle cx="5" cy="5" r="4"/><path d="M5 2.5V5h2"/></svg></span><span>monday – friday:10:00 – 16:00<br>saturday:12:00 – 15:00 sunday &amp;<br>holidays:09:00 – 12:00</span></div>
  </div>

  <div class="foot-col" style="left:829px">
    <h5>SUBSCRIBE TO OUR BLOG</h5>
    <p class="sub-text">Sign up today to get resources on how to attract and retain more customers!</p>
    <div class="sub-form">
      <div class="input">✉ Email Address</div>
      <div class="send"><svg width="16" height="16" viewBox="0 0 16 16" fill="#fff"><path d="M0 7L16 0 12 16 8 10z"/></svg></div>
    </div>
  </div>

  <div class="foot-bottom">
    <div class="copy">Copyright © 2020. Bravlo Pressure Washing Llc &nbsp;All Rights Reserved</div>
    <div class="legal">Terms and Conditions &nbsp;| &nbsp;Privacy Policy</div>
  </div>
</footer>

</body>
</html>
```